Pinecresttrips.com is a mountain biking and climbing travel company. We need a advertisement fo...

We need a advertisement for the back cover of a guide book. We would like a simple but strong ad that includes our logo. It must state that we are a biking and climbing company and people can contact us at the web site pinecresttrips.com We would like you to incorparate and below photo and logo on the ad.

```html
<!DOCTYPE html>
<html lang="en">
<head>
<meta charset="utf-8">
<title>Pinecrest Trips – Back Cover Ad</title>
<link href="https://fonts.googleapis.com/css2?family=Exo+2:ital,wght@0,400;0,600;0,800;1,900&family=Josefin+Sans:wght@400;600;700&display=swap" rel="stylesheet">
<style>
  :root {
    --backdrop: #4a4b4d;
    --ink: #111111;
    --tab: #1d1d1d;
    --gold: #e19b1e;
    --white: #ffffff;
    --street-warm: #7a5a3a;
    --street-dark: #2b2c30;
  }
  * { box-sizing: border-box; margin: 0; padding: 0; }
  html, body { width: 1200px; height: 862px; overflow: hidden; }
  body { background: var(--backdrop); font-family: "Josefin Sans", sans-serif; }

  .ad-page {
    position: absolute; left: 300px; top: 21px;
    width: 600px; height: 820px; overflow: hidden;
    background: var(--street-dark);
    box-shadow: 0 10px 30px rgba(0,0,0,.45);
  }
  .hero-photo {
    position: absolute; left: 0; top: 70px; width: 600px; height: 560px;
    background:
      radial-gradient(ellipse at 45% 20%, rgba(240,180,90,.75) 0%, rgba(160,110,60,.35) 30%, transparent 60%),
      radial-gradient(ellipse at 85% 40%, rgba(230,215,190,.5) 0%, transparent 45%),
      linear-gradient(180deg, var(--street-warm) 0%, #4d4740 45%, #5d5e62 75%, #6a6b6e 100%);
  }
  .header-band { position: absolute; left: 0; top: 0; width: 600px; height: 260px; }

  .brand {
    position: absolute; right: 40px; top: 42px;
    display: flex; align-items: center; gap: 12px; color: var(--white);
  }
  .brand-dot { width: 30px; height: 30px; border-radius: 50%; background: var(--white); }
  .brand-name { font-family: "Exo 2", sans-serif; font-weight: 600; font-size: 34px; letter-spacing: 1px; line-height: 1; }
  .brand-tag { position: absolute; right: 40px; top: 84px; color: var(--white); font-size: 12px; letter-spacing: 5px; }

  .headline {
    position: absolute; left: 0; width: 600px; top: 250px; text-align: center;
    font-family: "Exo 2", sans-serif; font-style: italic; font-weight: 900;
    font-size: 54px; color: var(--white); letter-spacing: 1px;
    text-shadow: 0 2px 8px rgba(0,0,0,.5);
  }
  .subhead {
    position: absolute; left: 160px; top: 322px; width: 280px; height: 46px;
    background: var(--tab); color: var(--white); text-align: center;
    font-size: 22px; letter-spacing: 2px; line-height: 50px;
  }

  .tour-card { position: absolute; width: 170px; }
  .tour-photo { height: 112px; border: 3px solid var(--white); }
  .tour-label {
    background: var(--tab); color: var(--white); text-align: center;
    font-size: 12px; line-height: 1.25; padding: 9px 6px 8px; text-transform: uppercase;
  }
  .card-bike { left: 38px; top: 470px; }
  .card-bike .tour-photo { background: linear-gradient(180deg, #6f9ccf 0%, #a8c2d8 45%, #8a8a50 60%, #6c7438 100%); }
  .card-climb { left: 218px; top: 520px; }
  .card-climb .tour-photo { background: linear-gradient(120deg, #8f7a62 0%, #6b5a48 45%, #4d5a36 80%, #3f4a2c 100%); }
  .card-custom { left: 398px; top: 570px; }
  .card-custom .tour-photo { background: linear-gradient(180deg, #4e8fd8 0%, #9cc5ea 40%, #7aa3b5 55%, #b3aa98 75%, #8d8a80 100%); }

  .contact-band { position: absolute; left: 0; top: 590px; width: 600px; height: 230px; }

  .book-tag { position: absolute; left: 30px; top: 690px; }
  .book-tag span {
    position: absolute; left: 0; top: 14px; width: 150px; text-align: center;
    font-family: "Exo 2", sans-serif; font-weight: 800; font-style: italic;
    font-size: 22px; line-height: 1.05; color: var(--white); text-transform: uppercase;
  }

  .contact { position: absolute; left: 215px; top: 720px; color: var(--ink); }
  .contact-row { display: flex; align-items: center; gap: 12px; }
  .phone { font-family: "Exo 2", sans-serif; font-weight: 800; font-size: 26px; }
  .web { margin-top: 6px; font-size: 22px; }
  .web b { font-weight: 700; }
</style>
</head>
<body>
  <main class="ad-page">
    <div class="hero-photo" role="img" aria-label="Photo of a narrow cobbled old-town street at dusk with warm lamplight and a blurred cyclist riding past"></div>

    <svg class="header-band" viewBox="0 0 600 260" aria-hidden="true">
      <path d="M0 0 H600 V250 C520 215 420 170 300 150 C180 130 90 125 0 130 Z" fill="var(--ink)"/>
    </svg>

    <div class="brand">
      <span class="brand-dot"></span>
      <span class="brand-name">PINECREST</span>
    </div>
    <div class="brand-tag">CLIMBING + RIDING</div>

    <h1 class="headline">PINECREST TRIPS</h1>
    <div class="subhead">CLIMBING + RIDING</div>

    <svg class="contact-band" viewBox="0 0 600 230" aria-hidden="true">
      <path d="M0 20 L600 110 V230 H0 Z" fill="var(--gold)"/>
    </svg>

    <article class="tour-card card-bike">
      <div class="tour-photo" role="img" aria-label="Photo of mountain bikers resting on a grassy ridge under a blue sky"></div>
      <p class="tour-label">Bike tour<br>March 10, 2019</p>
    </article>
    <article class="tour-card card-climb">
      <div class="tour-photo" role="img" aria-label="Photo of a climber on a sunlit limestone rock face"></div>
      <p class="tour-label">Climbing tour<br>April 14, 2019</p>
    </article>
    <article class="tour-card card-custom">
      <div class="tour-photo" role="img" aria-label="Photo of a coastal bay with a beach, cliffs and blue sky"></div>
      <p class="tour-label">Tailor-made tours<br>Flexible</p>
    </article>

    <div class="book-tag">
      <svg width="170" height="76" viewBox="0 0 170 76" aria-hidden="true">
        <path d="M0 0 H150 L170 38 L150 76 H0 Z" fill="var(--tab)"/>
      </svg>
      <span>Book<br>tour now</span>
    </div>

    <div class="contact">
      <div class="contact-row">
        <svg width="22" height="22" viewBox="0 0 24 24" aria-hidden="true">
          <circle cx="12" cy="12" r="10.5" fill="none" stroke="var(--ink)" stroke-width="2"/>
          <path d="M9 7 L10.5 10 L9.5 11 C10 12.5 11.5 14 13 14.5 L14 13.5 L17 15 L16 17 C12 17 7 12 7 8 Z" fill="var(--ink)"/>
        </svg>
        <span class="phone">+41 79 555 0142</span>
      </div>
      <div class="contact-row web">
        <svg width="22" height="22" viewBox="0 0 24 24" aria-hidden="true">
          <g fill="none" stroke="var(--ink)" stroke-width="1.8">
            <circle cx="12" cy="12" r="10"/>
            <ellipse cx="12" cy="12" rx="4.5" ry="10"/>
            <path d="M2 12 H22 M4 7 H20 M4 17 H20"/>
          </g>
        </svg>
        <span>www.<b>pinecresttrips</b>.com</span>
      </div>
    </div>
  </main>
</body>
</html>
```